Relaunch configurator for lighting

We just need a new modern design for our configurator
http://lichtkonfigurator.velmo.at

Design must be responsive

Number of Pages Required

1 page

```html
<!DOCTYPE html>
<html lang="en">
<head>
<meta charset="utf-8">
<title>Configurator – LED Solutions</title>
<link rel="stylesheet" href="https://fonts.googleapis.com/css2?family=Lato:ital,wght@0,400;0,700;0,900;1,400&display=swap">
<style>
:root{
  --orange:#f07524;
  --red:#9b1c1c;
  --ink:#2b2b2b;
  --muted:#555;
  --line:#d6d6d6;
  --band:#f5f5f5;
  --white:#fff;
  --dark-btn:#555;
}
*{box-sizing:border-box;margin:0;padding:0}
html,body{width:811px;height:1200px;overflow:hidden;background:var(--white)}
body{position:relative;font-family:"Lato",sans-serif;color:var(--ink)}
.abs{position:absolute}
.hero{left:0;top:0;width:811px;height:285px;
  background:linear-gradient(180deg,#d9d7d3 0%,#eceae6 45%,#c9c2b6 100%);
  clip-path:polygon(0 0,100% 0,100% 244px,50% 285px,0 244px)}
.hero-title{left:0;width:811px;text-align:center;color:var(--white);font-weight:900;line-height:1}
.hero-title.main{top:60px;font-size:56px;letter-spacing:.5px}
.hero-title.sub{top:117px;font-size:36px}
.section-title{top:323px;left:0;width:811px;text-align:center;font-size:19px;font-weight:700;letter-spacing:.3px}
.diagram{left:72px;top:366px;width:666px;height:76px;background:linear-gradient(90deg,#f4eaea,#faf4f4);border-radius:3px}
.check{width:13px;height:13px}
.opt-label{font-size:15px;font-weight:700;letter-spacing:.2px}
.note{font-size:11px;color:var(--red)}
.select{border:1px solid #bbb;background:var(--white);font-size:12px;font-weight:700;display:flex;align-items:center;justify-content:space-between;padding:0 8px 0 9px}
.select svg{width:8px;height:6px}
.panel{left:50px;top:515px;width:711px;height:274px;border:1px solid var(--line);border-radius:8px}
.panel-head{left:0;top:0;width:100%;height:50px;border-bottom:1px solid var(--line)}
.lamp-title{left:17px;top:16px;font-size:15px;font-weight:700}
.lamp-title span{color:var(--red)}
.btn{color:var(--white);font-size:13px;display:flex;align-items:center;justify-content:center;border-radius:2px}
.btn.orange{background:var(--orange)}
.btn.dark{background:var(--dark-btn)}
.sub-title{font-size:15px;color:var(--muted);font-weight:700}
.num{width:25px;height:25px;border:1px solid var(--red);border-radius:50%;font-size:11px;display:flex;align-items:center;justify-content:center;color:var(--muted)}
.profiles{left:384px;top:84px;width:270px;height:60px;background:linear-gradient(180deg,#f1f1f1,#d8d8d8)}
.divider{left:0;width:100%;height:1px;background:var(--line)}
.small{font-size:11.5px;font-weight:700;line-height:17px}
.cable-box{left:275px;top:194px;width:419px;height:57px;border:1px solid #999;border-radius:10px;overflow:hidden}
.cable-art{left:27px;top:11px;width:364px;height:36px;background:linear-gradient(90deg,#f4eaea,#fbf6f6)}
.card{top:824px;height:67px;border:1px solid var(--line)}
.card-art{left:8px;top:12px;width:80px;height:42px;border-radius:4px}
.card-label{font-size:10.5px;line-height:13px}
.band{left:0;top:932px;width:811px;height:210px;background:var(--band)}
.field{background:var(--white);border:1px solid var(--line);font-size:11.5px;font-weight:700;padding:0 11px}
.field em{font-weight:400;color:var(--red);font-size:9.5px;margin-left:4px}
.to-top{left:759px;top:1100px;width:24px;height:24px;border-radius:50%;background:#222}
.footer{left:50px;top:1165px;font-size:9.5px;color:#444;word-spacing:1px}
</style>
</head>
<body>

<header>
  <div class="abs hero" role="img" aria-label="Bright white kitchen interior with pendant lights"></div>
  <h1 class="abs hero-title main">CONFIGURATOR</h1>
  <p class="abs hero-title sub">LED SOLUTIONS</p>
</header>

<h2 class="abs section-title">CURRENT CONFIGURATION</h2>
<div class="abs diagram" role="img" aria-label="Wiring diagram: plug, power adapter, receiver and light bar with cable lengths"></div>

<!-- option row -->
<svg class="abs check" style="left:50px;top:461px" viewBox="0 0 13 13"><rect x=".75" y=".75" width="11.5" height="11.5" fill="none" stroke="#333" stroke-width="1.5"/><path d="M3 6.5l2.5 2.5L10 4" fill="none" stroke="#333" stroke-width="1.5"/></svg>
<div class="abs opt-label" style="left:80px;top:458px">Schuko plug</div>

<svg class="abs check" style="left:203px;top:452px" viewBox="0 0 13 13"><rect x=".75" y=".75" width="11.5" height="11.5" fill="none" stroke="#333" stroke-width="1.5"/><path d="M3 6.5l2.5 2.5L10 4" fill="none" stroke="#333" stroke-width="1.5"/></svg>
<div class="abs opt-label" style="left:232px;top:449px">Power adapter</div>
<div class="abs note" style="left:203px;top:470px">The power is calculated automatically</div>

<svg class="abs check" style="left:422px;top:462px" viewBox="0 0 13 13"><rect x=".75" y=".75" width="11.5" height="11.5" fill="none" stroke="#333" stroke-width="1.5"/><path d="M3 6.5l2.5 2.5L10 4" fill="none" stroke="#333" stroke-width="1.5"/></svg>
<div class="abs opt-label" style="left:452px;top:459px">Receiver</div>

<div class="abs opt-label" style="left:540px;top:458px">Number of lights (1-12)</div>
<div class="abs select" style="left:704px;top:456px;width:57px;height:23px">1<svg viewBox="0 0 8 6"><path d="M1 1l3 3 3-3" fill="none" stroke="#222" stroke-width="1.6"/></svg></div>

<!-- lamp panel -->
<section class="abs panel">
  <div class="abs panel-head">
    <div class="abs lamp-title">LAMP <span>10 mm / 0 Watt</span></div>
    <div class="abs btn orange" style="left:436px;top:12px;width:130px;height:27px">Close the Lamp</div>
    <div class="abs btn orange" style="left:571px;top:12px;width:130px;height:27px">New Configurator</div>
  </div>

  <div class="abs sub-title" style="left:17px;top:67px">Profile / Spot</div>
  <div class="abs select" style="left:18px;top:103px;width:268px;height:30px;border-color:#ccc;font-size:11.5px">Select<svg viewBox="0 0 8 6"><path d="M1 1l3 3 3-3" fill="none" stroke="#222" stroke-width="1.6"/></svg></div>
  <div class="abs num" style="left:386px;top:61px">1</div>
  <div class="abs num" style="left:435px;top:61px">2</div>
  <div class="abs num" style="left:488px;top:61px">3</div>
  <div class="abs num" style="left:546px;top:61px">4</div>
  <div class="abs num" style="left:621px;top:61px">5</div>
  <div class="abs profiles" role="img" aria-label="Five aluminium profile options"></div>

  <div class="abs divider" style="top:169px"></div>

  <div class="abs sub-title" style="left:17px;top:195px">Connecting cable</div>
  <svg class="abs" style="left:159px;top:197px;width:14px;height:14px" viewBox="0 0 14 14"><rect x=".75" y=".75" width="12.5" height="12.5" fill="none" stroke="#9b1c1c" stroke-width="1.5"/><path d="M4.5 4.5l5 5M9.5 4.5l-5 5" stroke="#9b1c1c" stroke-width="1.6"/></svg>
  <div class="abs select" style="left:20px;top:217px;width:57px;height:24px">1<svg viewBox="0 0 8 6"><path d="M1 1l3 3 3-3" fill="none" stroke="#222" stroke-width="1.6"/></svg></div>
  <div class="abs small" style="left:87px;top:219px">mm</div>
  <div class="abs small" style="left:131px;top:218px">Cable length<br>(500 mm - 9500 mm)</div>
  <div class="abs cable-box">
    <div class="abs cable-art" role="img" aria-label="Cable length diagram with connector and light bar"></div>
  </div>
</section>

<!-- controller -->
<svg class="abs check" style="left:50px;top:832px" viewBox="0 0 13 13"><rect x=".75" y=".75" width="11.5" height="11.5" fill="none" stroke="#333" stroke-width="1.5"/><path d="M3 6.5l2.5 2.5L10 4" fill="none" stroke="#333" stroke-width="1.5"/></svg>
<div class="abs opt-label" style="left:80px;top:829px">Controller</div>
<svg class="abs" style="left:169px;top:831px;width:14px;height:14px" viewBox="0 0 14 14"><circle cx="7" cy="7" r="7" fill="#9b1c1c"/><circle cx="7" cy="4" r="1.2" fill="#fff"/><rect x="6" y="6" width="2" height="5" fill="#fff"/></svg>
<div class="abs small" style="left:80px;top:856px">Number /<br>color (max. 8 pieces)</div>

<div class="abs card" style="left:203px;width:180px">
  <div class="abs card-art" role="img" aria-label="White controller" style="background:linear-gradient(135deg,#fafafa,#e3e3e3)"></div>
  <div class="abs card-label" style="left:95px;top:17px">White</div>
  <div class="abs select" style="left:95px;top:30px;width:57px;height:23px">1<svg viewBox="0 0 8 6"><path d="M1 1l3 3 3-3" fill="none" stroke="#222" stroke-width="1.6"/></svg></div>
</div>
<div class="abs card" style="left:392px;width:180px">
  <div class="abs card-art" role="img" aria-label="Aluminium coloured controller" style="background:linear-gradient(135deg,#eee,#c9c9c9)"></div>
  <div class="abs card-label" style="left:95px;top:11px">Aluminum<br>colored</div>
  <div class="abs select" style="left:95px;top:37px;width:57px;height:23px">1<svg viewBox="0 0 8 6"><path d="M1 1l3 3 3-3" fill="none" stroke="#222" stroke-width="1.6"/></svg></div>
</div>
<div class="abs card" style="left:581px;width:180px">
  <div class="abs card-art" role="img" aria-label="Nickel matt controller" style="background:linear-gradient(135deg,#f1ebdd,#d4c6a6)"></div>
  <div class="abs card-label" style="left:95px;top:17px">Nickel matt</div>
  <div class="abs select" style="left:95px;top:30px;width:57px;height:23px">1<svg viewBox="0 0 8 6"><path d="M1 1l3 3 3-3" fill="none" stroke="#222" stroke-width="1.6"/></svg></div>
</div>

<!-- notes band -->
<div class="abs band"></div>
<div class="abs field" style="left:202px;top:960px;width:408px;height:34px;display:flex;align-items:center">Packaging lettering<em>(Max. 20 characters)</em></div>
<div class="abs field" style="left:202px;top:1003px;width:408px;height:74px;padding-top:10px">Personal notes</div>
<div class="abs btn dark" style="left:274px;top:1087px;width:130px;height:28px">Reset</div>
<div class="abs btn orange" style="left:408px;top:1087px;width:129px;height:28px">Configuration Lamp</div>
<svg class="abs to-top" viewBox="0 0 24 24"><path d="M6.5 14.5L12 9l5.5 5.5" fill="none" stroke="#fff" stroke-width="3" stroke-linecap="round" stroke-linejoin="round"/></svg>

<footer class="abs footer">Copyright ©2020&nbsp; CompanyName . All Right Reserved&nbsp;&nbsp; Terms &amp; Conditions&nbsp;&nbsp;&nbsp; Privacy</footer>

</body>
</html>
```